Pictures to represent a consulting company and their main topics

We need around 10 pictures which can be used in blogs, webpages, powerpoints or articles to prettify and visualize the content.
We are a business consulting company in the financial industry.
We are based in and focussed on Switzerland.
Our main colours are blue turquise and grey (see www.veltrano.example).
The main topics, we would like to use the pictures for are:
- Digitalization
- Regulations
- Agile Project Management
- Advisory Process
- Automated System Testing
The price is for 10 pictures (which should be similar and therefore are not considered as 10 independent projects).
We propose to start with 3 example pictures to agree on the style. The rest will then be similar ones of the same style.
I have added examples from other companies.
It can be based on stock images or (prefferably) sketched images. Important is that the style is always the same.
Target Market(s)
Banking and Banking Consulting Market Switzerland
Industry/Entity Type
Business

```html
<!DOCTYPE html>
<html lang="en">
<head>
<meta charset="utf-8">
<title>Veltrano Consulting – Topic Banners</title>
<link rel="stylesheet" href="https://fonts.googleapis.com/css2?family=Oswald:wght@400;500&display=swap">
<style>
  :root {
    --backdrop-light: #fafafa;
    --backdrop-dark: #cdcdcd;
    --navy: #123f82;
    --blue: #2c5b9b;
    --blue-soft: rgba(44, 91, 155, 0.78);
    --white: #ffffff;
    --brand: #1d3f7c;
  }
  html, body {
    margin: 0;
    padding: 0;
    width: 1200px;
    height: 1200px;
    overflow: hidden;
  }
  .board {
    position: relative;
    width: 1200px;
    height: 1200px;
    background: radial-gradient(ellipse at 50% 60%, var(--backdrop-light) 0%, #e6e6e6 55%, var(--backdrop-dark) 100%);
  }
  .banner {
    position: absolute;
    width: 545px;
    height: 221px;
    overflow: hidden;
    background: var(--white);
  }
  .banner svg { display: block; width: 100%; height: 100%; }
  .banner--regulations { left: 58px; top: 239px; }
  .banner--agile { left: 626px; top: 239px; }
  .banner--testing { left: 58px; top: 555px; }
  .banner--digital { left: 626px; top: 555px; }
  .banner--advisory { left: 311px; top: 839px; }
  .headline {
    font-family: "Oswald", sans-serif;
    font-weight: 500;
    fill: var(--white);
  }
  .brand-name {
    font-family: "Oswald", sans-serif;
    font-weight: 400;
    fill: var(--brand);
  }
</style>
</head>
<body>
<main class="board">
  <svg width="0" height="0" style="position:absolute" aria-hidden="true">
    <defs>
      <linearGradient id="light-band" x1="0" y1="0" x2="1" y2="0">
        <stop offset="0" stop-color="#ffffff" stop-opacity="0.3"/>
        <stop offset="1" stop-color="#ffffff" stop-opacity="0"/>
      </linearGradient>
      <radialGradient id="glow" cx="0.5" cy="0.5" r="0.5">
        <stop offset="0" stop-color="#ffffff" stop-opacity="0.35"/>
        <stop offset="1" stop-color="#ffffff" stop-opacity="0"/>
      </radialGradient>
      <radialGradient id="shade" cx="0.5" cy="0.5" r="0.5">
        <stop offset="0" stop-color="#000000" stop-opacity="0.35"/>
        <stop offset="1" stop-color="#000000" stop-opacity="0"/>
      </radialGradient>
    </defs>
  </svg>

  <!-- Regulations -->
  <section class="banner banner--regulations">
    <svg viewBox="0 0 681 276" preserveAspectRatio="none">
      <defs>
        <linearGradient id="photo-cool" x1="0" y1="0" x2="1" y2="1">
          <stop offset="0" stop-color="#c3d6e6"/>
          <stop offset="0.45" stop-color="#5a7f9d"/>
          <stop offset="1" stop-color="#1e3550"/>
        </linearGradient>
      </defs>
      <g role="img" aria-label="Photo of office binders labelled regulations on a shelf">
        <rect width="681" height="276" fill="url(#photo-cool)"/>
        <ellipse cx="120" cy="40" rx="200" ry="80" fill="url(#glow)"/>
        <ellipse cx="330" cy="170" rx="180" ry="70" fill="url(#shade)"/>
      </g>
      <polygon points="400,0 681,0 681,5 530,95" fill="var(--white)"/>
      <polygon points="681,5 681,276 240,276" fill="var(--navy)"/>
      <polygon points="681,5 681,200 470,120" fill="var(--blue-soft)"/>
      <polygon points="0,115 245,276 0,276" fill="var(--white)"/>
      <rect x="300" y="188" width="381" height="40" fill="url(#light-band)"/>
      <text class="headline" x="406" y="229" font-size="50" textLength="232" lengthAdjust="spacingAndGlyphs">REGULATIONS</text>
      <g class="brand">
        <rect x="22" y="214" width="18" height="18" fill="var(--brand)"/>
        <text class="brand-name" x="48" y="238" font-size="26" letter-spacing="2">VELTRANO</text>
        <text class="brand-name" x="48" y="258" font-size="16" letter-spacing="0.5">Consulting AG</text>
      </g>
    </svg>
  </section>

  <!-- Agile -->
  <section class="banner banner--agile">
    <svg viewBox="0 0 681 276" preserveAspectRatio="none">
      <defs>
        <linearGradient id="photo-wood" x1="0" y1="0" x2="1" y2="1">
          <stop offset="0" stop-color="#c99a63"/>
          <stop offset="0.6" stop-color="#9a6a3b"/>
          <stop offset="1" stop-color="#4b3a33"/>
        </linearGradient>
      </defs>
      <g role="img" aria-label="Photo of a team working with charts and documents on a wooden meeting table">
        <rect width="681" height="276" fill="url(#photo-wood)"/>
        <ellipse cx="420" cy="150" rx="160" ry="90" fill="url(#glow)"/>
        <ellipse cx="620" cy="250" rx="120" ry="60" fill="url(#shade)"/>
      </g>
      <polygon points="450,0 681,0 681,140" fill="var(--white)"/>
      <polygon points="0,0 460,276 0,276" fill="var(--navy)"/>
      <polygon points="0,0 300,180 0,180" fill="var(--blue-soft)"/>
      <rect x="0" y="150" width="420" height="90" fill="url(#light-band)"/>
      <text class="headline" x="32" y="216" font-size="82" textLength="160" lengthAdjust="spacingAndGlyphs">AGILE</text>
      <text class="headline" x="32" y="242" font-size="20" textLength="166" lengthAdjust="spacingAndGlyphs">PROJECT MANAGEMENT</text>
      <g class="brand">
        <rect x="528" y="22" width="18" height="18" fill="var(--brand)"/>
        <text class="brand-name" x="554" y="45" font-size="26" letter-spacing="2">VELTRANO</text>
        <text class="brand-name" x="554" y="65" font-size="16" letter-spacing="0.5">Consulting AG</text>
      </g>
    </svg>
  </section>

  <!-- Automated System Testing -->
  <section class="banner banner--testing">
    <svg viewBox="0 0 681 276" preserveAspectRatio="none">
      <defs>
        <linearGradient id="photo-machine" x1="0" y1="0" x2="1" y2="1">
          <stop offset="0" stop-color="#4a5a6c"/>
          <stop offset="0.5" stop-color="#9aa3a8"/>
          <stop offset="1" stop-color="#1c1f24"/>
        </linearGradient>
      </defs>
      <g role="img" aria-label="Photo of an engineer in a hard hat operating an industrial control panel">
        <rect width="681" height="276" fill="url(#photo-machine)"/>
        <ellipse cx="400" cy="90" rx="140" ry="80" fill="url(#glow)"/>
        <ellipse cx="560" cy="220" rx="150" ry="70" fill="url(#shade)"/>
      </g>
      <polygon points="430,0 681,0 681,210" fill="var(--white)"/>
      <polygon points="0,0 30,0 420,276 0,276" fill="var(--navy)"/>
      <polygon points="0,0 160,60 260,276 0,276" fill="var(--blue-soft)"/>
      <rect x="0" y="168" width="440" height="80" fill="url(#light-band)"/>
      <text class="headline" x="58" y="212" font-size="50" textLength="174" lengthAdjust="spacingAndGlyphs">AUTOMATED</text>
      <text class="headline" x="58" y="246" font-size="38" textLength="176" lengthAdjust="spacingAndGlyphs">SYSTEM TESTING</text>
      <g class="brand">
        <rect x="520" y="26" width="18" height="18" fill="var(--brand)"/>
        <text class="brand-name" x="546" y="49" font-size="26" letter-spacing="2">VELTRANO</text>
        <text class="brand-name" x="546" y="69" font-size="16" letter-spacing="0.5">Consulting AG</text>
      </g>
    </svg>
  </section>

  <!-- Digitalization -->
  <section class="banner banner--digital">
    <svg viewBox="0 0 681 276" preserveAspectRatio="none">
      <defs>
        <linearGradient id="photo-digital" x1="0" y1="0" x2="1" y2="1">
          <stop offset="0" stop-color="#7fa6b8"/>
          <stop offset="0.5" stop-color="#3f6c82"/>
          <stop offset="1" stop-color="#163042"/>
        </linearGradient>
      </defs>
      <g role="img" aria-label="Photo of business people in a modern hall with glowing digital interface elements">
        <rect width="681" height="276" fill="url(#photo-digital)"/>
        <ellipse cx="560" cy="110" rx="140" ry="80" fill="url(#glow)"/>
        <ellipse cx="420" cy="200" rx="120" ry="70" fill="url(#shade)"/>
      </g>
      <polygon points="0,0 480,0 235,100" fill="var(--white)"/>
      <polygon points="615,276 681,276 681,190" fill="var(--white)"/>
      <polygon points="0,0 235,100 615,276 0,276" fill="var(--navy)" opacity="0.9"/>
      <polygon points="0,0 235,100 330,276 0,276" fill="var(--blue)"/>
      <rect x="0" y="185" width="500" height="50" fill="url(#light-band)"/>
      <text class="headline" x="45" y="234" font-size="54" textLength="232" lengthAdjust="spacingAndGlyphs">DIGITALIZATION</text>
      <g class="brand">
        <rect x="160" y="20" width="18" height="18" fill="var(--brand)"/>
        <text class="brand-name" x="186" y="43" font-size="26" letter-spacing="2">VELTRANO</text>
        <text class="brand-name" x="186" y="63" font-size="16" letter-spacing="0.5">Consulting AG</text>
      </g>
    </svg>
  </section>

  <!-- Advisory Process -->
  <section class="banner banner--advisory">
    <svg viewBox="0 0 681 276" preserveAspectRatio="none">
      <defs>
        <linearGradient id="photo-office" x1="0" y1="0" x2="1" y2="1">
          <stop offset="0" stop-color="#dfe4e8"/>
          <stop offset="0.5" stop-color="#8c959c"/>
          <stop offset="1" stop-color="#3a3f46"/>
        </linearGradient>
      </defs>
      <g role="img" aria-label="Photo of a group of colleagues talking in a bright office">
        <rect width="681" height="276" fill="url(#photo-office)"/>
        <ellipse cx="500" cy="60" rx="180" ry="70" fill="url(#glow)"/>
        <ellipse cx="420" cy="190" rx="160" ry="70" fill="url(#shade)"/>
      </g>
      <polygon points="0,0 300,0 190,65" fill="var(--white)"/>
      <polygon points="455,276 681,276 681,118" fill="var(--white)"/>
      <polygon points="0,0 190,65 620,276 0,276" fill="var(--navy)" opacity="0.9"/>
      <polygon points="0,0 190,65 330,276 0,276" fill="var(--blue)"/>
      <rect x="0" y="185" width="540" height="50" fill="url(#light-band)"/>
      <text class="headline" x="38" y="234" font-size="54" textLength="310" lengthAdjust="spacingAndGlyphs">ADVISORY PROCESS</text>
      <g class="brand">
        <rect x="532" y="192" width="18" height="18" fill="var(--brand)"/>
        <text class="brand-name" x="558" y="215" font-size="26" letter-spacing="2">VELTRANO</text>
        <text class="brand-name" x="558" y="235" font-size="16" letter-spacing="0.5">Consulting AG</text>
      </g>
    </svg>
  </section>

</main>
</body>
</html>
```